Business card for Clear Harbour Lending

Front (space for each) - Name, title, qualifications, mobile number, email address, website, name/logo,
Back - Business name/logo and slogan "your dream is our vision" underneath,
in small writing underneath need ABN number, CRN number, ACL number
Target Market(s)
First Home Buyers
Industry/Entity Type
Finance
Contact Information for Business Card
Requirements
Must have
- Front (space for each) - Name, title, qualifications, mobile number, email address, website, name/logo,

```html
<!DOCTYPE html>
<html lang="en">
<head>
<meta charset="UTF-8">
<title>Clear Harbour Lending – Business Card</title>
<link href="https://fonts.googleapis.com/css2?family=Montserrat:wght@400;500;700&display=swap" rel="stylesheet">
<style>
  :root {
    --stage: #1d1d20;
    --lime: #8cc84b;
    --teal: #12aca0;
    --teal-deep: #0fa6a6;
    --ink: #1a1a1a;
    --body: #2a2a2a;
    --white: #ffffff;
    --amber: #f0b43c;
    --coral: #ec5a3a;
  }
  * { margin: 0; padding: 0; box-sizing: border-box; }
  html, body {
    width: 1200px; height: 948px; overflow: hidden;
    background: var(--stage);
    font-family: "Montserrat", Arial, sans-serif;
  }
  .stage {
    width: 1200px; height: 948px;
    display: flex; flex-direction: column; align-items: center; justify-content: center;
    gap: 40px;
  }
  .card {
    width: 720px; height: 411px;
    border-radius: 28px;
    position: relative; overflow: hidden;
  }

  /* Shared name block */
  .brand {
    display: flex; align-items: center; gap: 14px;
    font-weight: 500; white-space: nowrap;
  }
  .brand__mark { width: 16px; height: 16px; flex: none; }

  /* Back side */
  .card--back {
    background: linear-gradient(170deg, var(--lime) 0%, #3fbb7f 45%, var(--teal) 75%, var(--teal-deep) 100%);
    color: var(--white);
    display: flex; flex-direction: column; align-items: center; justify-content: center;
  }
  .card--back .brand { font-size: 38px; }
  .card--back .brand__mark { background: var(--white); }
  .slogan {
    margin-top: 40px;
    font-size: 24px; font-weight: 500; letter-spacing: 0.03em; text-transform: uppercase;
  }
  .registrations {
    margin-top: 12px;
    font-size: 15px; font-weight: 500; letter-spacing: 0.04em;
  }

  /* Front side */
  .card--front {
    background: var(--white);
    display: flex; align-items: center;
  }
  .card--front::after {
    content: ""; position: absolute; left: 0; right: 0; bottom: 0; height: 12px;
    background: linear-gradient(90deg, var(--teal-deep), var(--lime));
  }
  .front-brand {
    width: 330px; display: flex; justify-content: center;
  }
  .front-brand .brand { font-size: 22px; color: var(--ink); gap: 10px; }
  .front-brand .brand__mark { width: 12px; height: 12px; background: var(--teal); }
  .divider {
    width: 2px; height: 210px;
    background: linear-gradient(180deg, var(--amber), var(--coral));
  }
  .contact { padding-left: 34px; color: var(--body); }
  .contact__name {
    font-size: 28px; font-weight: 700; letter-spacing: 0.02em; text-transform: uppercase;
    background: linear-gradient(90deg, var(--teal), var(--lime));
    -webkit-background-clip: text; background-clip: text; color: transparent;
  }
  .contact__title { font-size: 17px; margin-top: 2px; }
  .contact__quals { font-size: 14px; margin-top: 2px; color: #555; }
  .contact__address { font-size: 17px; margin-top: 16px; line-height: 1.35; }
  .contact__list { list-style: none; margin-top: 6px; font-size: 17px; line-height: 1.45; }
  .contact__list li { display: flex; align-items: center; gap: 10px; }
  .contact__list svg { width: 15px; height: 15px; flex: none; }
</style>
</head>
<body>
<main class="stage">
  <section class="card card--back" aria-label="Card back">
    <div class="brand"><span class="brand__mark"></span>Clear Harbour Lending</div>
    <p class="slogan">Your dream is our vision</p>
    <p class="registrations">ABN 121345 | CRN 121345 | ACL 121345</p>
  </section>

  <section class="card card--front" aria-label="Card front">
    <div class="front-brand">
      <div class="brand"><span class="brand__mark"></span>Clear Harbour Lending</div>
    </div>
    <div class="divider"></div>
    <div class="contact">
      <h1 class="contact__name">Daniel Reyes</h1>
      <p class="contact__title">Owner/CEO</p>
      <p class="contact__quals">Dip. Finance &amp; Mortgage Broking</p>
      <p class="contact__address">48 Wharf Road<br>Bayside District 4120</p>
      <ul class="contact__list">
        <li><svg viewBox="0 0 16 16" aria-hidden="true"><path fill="#2bb58a" d="M3 1.5l3 .5 1 3-1.8 1.3a8 8 0 0 0 4.5 4.5L11 9l3 1 .5 3-2 1.5C7 14 2 9 1.5 3.5z"/></svg>041-555-2087</li>
        <li><svg viewBox="0 0 16 16" aria-hidden="true"><rect x="1" y="3" width="14" height="10" rx="1" fill="#4fbf6a"/><path d="M1.5 3.8 8 9l6.5-5.2" stroke="#fff" stroke-width="1.3" fill="none"/></svg>info@clearharbourlending.com</li>
        <li><svg viewBox="0 0 16 16" aria-hidden="true"><circle cx="8" cy="8" r="7" fill="#3cb87c"/><path d="M1 8h14M8 1c-3 3.5-3 10.5 0 14M8 1c3 3.5 3 10.5 0 14" stroke="#fff" stroke-width="1" fill="none"/></svg>www.clearharbourlending.com</li>
      </ul>
    </div>
  </section>
</main>
</body>
</html>
```